Real Estate Brokerage Informational Handbill

A 4 X 6 handbill to promote a real estate brokerage modeled after the design attached including attached logo and information.
These handbills should provide a high-level overview of what we do at the brokerage and should be attractive and be inviting.
The goal of the handbill is to have motivated clients in the market to buy or sell their home or property call or visit our website

Target Market(s)

Buyers and sellers of real estate in the Rochester NY area ages 24 - 60

Industry/Entity Type

Real Estate

Font styles to use
Sans Serif

Requirements
Must have
• Please include all the information contained on current handbill
• remove the line "we will walk you through the home buying process at no cost to you".
• replace with "come to one of our monthly first-time buyer informational sessions".
• add the phrase "have your reviewed and receive customized Home Purchase Plan"
• Add the slogan "Bright Gate Realty Helping Motivated People Achieve Their Real Estate Goals"
Nice to have
• 2 sided design

```html
<!DOCTYPE html>
<html lang="en">
<head>
<meta charset="utf-8">
<title>Bright Gate Realty – Handbill</title>
<link rel="stylesheet" href="https://fonts.googleapis.com/css2?family=Crimson+Pro:wght@700&family=Lato:wght@700;900&display=swap">
<style>
  :root {
    --slate: #3e4858;
    --slate-dark: #2f3744;
    --pink: #c9517f;
    --rose: #e98aae;
    --maroon: #7b2c50;
    --ink: #262626;
    --paper: #f7f7f7;
    --paper-shade: #dcdcde;
    --white: #ffffff;
  }
  * { margin: 0; padding: 0; box-sizing: border-box; }
  html, body { width: 900px; height: 1200px; overflow: hidden; background: var(--paper); }
  .handbill {
    position: relative; width: 900px; height: 1200px; overflow: hidden;
    font-family: "Lato", Arial, sans-serif; color: var(--ink);
  }
  .handbill__shapes { position: absolute; inset: 0; }
  .brand-name {
    position: absolute; top: 112px; left: 0; width: 900px; text-align: center;
    font-family: "Lato", Arial, sans-serif; font-weight: 900; font-size: 54px;
    color: var(--rose); letter-spacing: 1px;
  }
  .title-banner {
    position: absolute; top: 318px; left: 110px; width: 680px; height: 56px;
    background: linear-gradient(90deg, var(--maroon) 0%, #9a3d66 50%, var(--maroon) 100%);
    box-shadow: 0 6px 10px rgba(0,0,0,.18);
    display: flex; align-items: center; justify-content: center;
  }
  .title-banner h1 {
    font-family: "Crimson Pro", Georgia, serif; font-weight: 700;
    font-size: 50px; color: var(--white); line-height: 1;
  }
  .tagline {
    position: absolute; top: 388px; left: 0; width: 900px; text-align: center;
    font-weight: 700; font-size: 24px; line-height: 30px; color: var(--ink);
  }
  .credit-callout {
    position: absolute; top: 484px; left: 84px; width: 732px; height: 76px;
    border: 2.5px solid var(--slate); border-radius: 22px;
    display: flex; align-items: center; justify-content: center; text-align: center;
    font-weight: 700; font-size: 22px; line-height: 29px; color: var(--ink);
  }
  .section-tag {
    position: absolute; top: 586px; height: 34px; width: 250px;
    display: flex; align-items: center;
    font-family: "Crimson Pro", Georgia, serif; font-weight: 700; font-size: 28px; color: var(--white);
  }
  .section-tag--left {
    left: 0; padding-left: 60px;
    background: linear-gradient(90deg, #e9a6c0, var(--maroon));
    clip-path: polygon(0 0, 92% 0, 100% 50%, 92% 100%, 0 100%);
  }
  .section-tag--right {
    right: 0; padding-left: 50px;
    background: linear-gradient(90deg, var(--maroon), #e9a6c0);
    clip-path: polygon(8% 0, 100% 0, 100% 100%, 8% 100%, 0 50%);
  }
  .service-list { position: absolute; list-style: none; font-weight: 700; font-size: 25px; line-height: 39px; }
  .service-list--left { top: 636px; left: 58px; }
  .service-list--right { top: 634px; right: 44px; text-align: right; }
  .service-list li { position: relative; }
  .service-list--left li { padding-left: 16px; }
  .service-list--right li { padding-right: 24px; }
  .service-list li.has-dot::before {
    content: ""; position: absolute; top: 16px; width: 9px; height: 9px; border-radius: 50%;
    background: var(--maroon);
  }
  .service-list--left li.has-dot::before { left: 0; }
  .service-list--right li.has-dot::before { right: 0; }
  .seller-call {
    position: absolute; top: 1042px; left: 0; width: 900px; text-align: center;
    font-weight: 700; font-size: 26px; line-height: 39px; font-variant: small-caps;
    color: var(--ink); letter-spacing: .5px;
  }
</style>
</head>
<body>
<main class="handbill">
  <svg class="handbill__shapes" width="900" height="1200" viewBox="0 0 900 1200" aria-hidden="true">
    <defs>
      <linearGradient id="paperFill" x1="0" y1="0" x2="1" y2="1">
        <stop offset="0" stop-color="#ffffff"/>
        <stop offset="0.6" stop-color="#f1f1f2"/>
        <stop offset="1" stop-color="#d9d9db"/>
      </linearGradient>
      <linearGradient id="headerPink" x1="0" y1="0" x2="1" y2="0">
        <stop offset="0" stop-color="#b8476f"/>
        <stop offset="0.5" stop-color="#e07ca2"/>
        <stop offset="1" stop-color="#b8476f"/>
      </linearGradient>
      <linearGradient id="footerPink" x1="0" y1="0" x2="1" y2="1">
        <stop offset="0" stop-color="#a33e66"/>
        <stop offset="0.55" stop-color="#e27fa5"/>
        <stop offset="1" stop-color="#ee8fb2"/>
      </linearGradient>
    </defs>
    <rect class="paper" width="900" height="1200" fill="url(#paperFill)"/>
    <path class="paper-fold" d="M300,300 C520,520 560,820 420,1050 L560,1050 C640,800 600,520 420,300Z" fill="#ffffff" opacity=".45"/>
    <path class="header-band" d="M0,0 H900 V120 C720,230 580,268 450,268 C320,268 180,230 0,120 Z" fill="var(--slate)"/>
    <path class="header-swoosh" d="M0,120 C180,230 320,268 450,268 C580,268 720,230 900,120 V200 C730,280 590,300 450,300 C310,300 170,280 0,200 Z" fill="url(#headerPink)"/>
    <path class="header-edge" d="M0,200 C170,280 310,300 450,300 C590,300 730,280 900,200 V228 C730,300 590,312 450,312 C310,312 170,300 0,228 Z" fill="#ffffff"/>
    <path class="footer-band" d="M0,905 C220,1010 680,1010 900,905 V1200 H0 Z" fill="url(#footerPink)"/>
    <path class="footer-edge" d="M0,905 C220,1010 680,1010 900,905 V918 C680,1020 220,1020 0,918 Z" fill="var(--maroon)" opacity=".55"/>
  </svg>

  <div class="brand-name">Bright Gate Realty</div>

  <div class="title-banner"><h1>Bright Gate Realty</h1></div>

  <p class="tagline">Making Rochester a better place by<br>Helping Motivated People Achieve Their Real Estate Goals</p>

  <div class="credit-callout">Have your credit reviewed and receive personalized<br>Home Purchase Plan?</div>

  <div class="section-tag section-tag--left">First Time</div>
  <div class="section-tag section-tag--right">First Time</div>

  <ul class="service-list service-list--left">
    <li class="has-dot">Buyer Grant Assistance</li>
    <li class="has-dot">Credit Counseling</li>
    <li class="has-dot">Rochester’s Best Realtors</li>
    <li class="has-dot">Customized Property Search</li>
    <li>Closing and</li>
    <li class="has-dot">Post-Closing Assistance</li>
  </ul>

  <ul class="service-list service-list--right">
    <li class="has-dot">Home Buyer’s Specialists</li>
    <li class="has-dot">Assisting you with all of</li>
    <li>your real estate needs from</li>
    <li>CREDIT to CLOSING and</li>
    <li class="has-dot">Beyond come to one of our</li>
    <li>monthly first-time buyer</li>
    <li>informational sessions</li>
  </ul>

  <p class="seller-call">Need to Sell your property<br>Call us today for a free consultation<br>Residential Investment Commercial</p>
</main>
</body>
</html>
```